Accounting Practice Business Card Design

I have a logo I am happy for you to use in the design of the Business Card.
You can edit and change colours as you please, I am not fixated on it.
I am looking for a modern and clean overall feel for the finished design.

The business is a small accounting practice who thrives on word of mouth referrals and this card will be given to all current and prospect clients.

Industry/Entity Type

Accountant

Contact Information for Business Card

Marcus Elwin
Level 5, 8 Corvale Ridge Road
ASHGROVE RISE VIC 3187
Phone: 9481 3057
Email: melwin@mrfaccountants.com.au
Web: www.mrfaccountants.com.au

Font styles to use
Serif
Sans Serif

Colors
0555a3
3277b5
85acd3
0393ce
33a6d7
85cae6
00a990
33b8a4
9bcb3c

Requirements
Must have
• "The end to your tax problems begin with us"
• "A referral from you is our greatest compliment"
Nice to have
• Modern clean professional

```html
<!DOCTYPE html>
<html lang="en">
<head>
<meta charset="utf-8">
<title>MRF Accountants – Business Card</title>
<link rel="stylesheet" href="https://fonts.googleapis.com/css2?family=Lato:wght@400;700;900&display=swap">
<style>
  :root {
    --backdrop: #2f2f2f;
    --navy: #264a7c;
    --green: #3b7a35;
    --ink: #1c1c1c;
    --paper: #ffffff;
  }
  * { margin: 0; padding: 0; box-sizing: border-box; }
  html, body { width: 1200px; height: 1200px; overflow: hidden; }
  body {
    background: radial-gradient(circle at 50% 45%, #3a3a3a, var(--backdrop) 75%);
    font-family: "Lato", sans-serif;
    position: relative;
  }
  .card {
    position: absolute;
    left: 150px;
    width: 900px;
    height: 514px;
    overflow: hidden;
    box-shadow: 0 18px 40px rgba(0,0,0,.45);
  }
  .card--back { top: 66px; background: var(--navy); color: var(--paper); }
  .card--front { top: 620px; background: var(--paper); color: var(--ink); }

  .brand {
    position: absolute;
    font-weight: 900;
    line-height: .9;
    text-align: center;
  }
  .brand__mark { display: block; font-size: 150px; letter-spacing: 4px; }
  .brand__word { display: block; font-size: 40px; letter-spacing: 3px; margin-top: 10px; }
  .card--back .brand { left: 0; right: 0; top: 120px; color: var(--paper); }

  .tagline {
    position: absolute;
    left: 0; right: 0;
    text-align: center;
    font-size: 24px;
    letter-spacing: 1px;
    text-transform: uppercase;
  }
  .card--back .tagline { bottom: 62px; }

  .card--front .brand { left: 60px; width: 380px; top: 150px; color: var(--navy); }
  .card--front .brand__mark { font-size: 130px; }
  .card--front .brand__word { font-size: 36px; }

  .divider {
    position: absolute;
    left: 470px; top: 110px;
    width: 3px; height: 220px;
    background: var(--navy);
  }
  .contact { position: absolute; left: 505px; top: 100px; }
  .contact__name { font-size: 34px; font-weight: 700; color: var(--green); }
  .contact__role { font-size: 22px; margin-top: 2px; }
  .contact__address { font-size: 22px; line-height: 1.3; margin-top: 12px; }
  .contact__lines { list-style: none; margin-top: 12px; font-size: 22px; line-height: 1.35; }
  .contact__lines li { display: flex; align-items: center; gap: 14px; }
  .contact__lines svg { width: 20px; height: 20px; fill: var(--green); flex: none; }

  .card--front .tagline { bottom: 58px; color: var(--ink); }
  .base-band { position: absolute; left: 0; right: 0; bottom: 0; height: 14px; background: var(--navy); }
</style>
</head>
<body>
  <section class="card card--back" aria-label="Card back">
    <div class="brand">
      <span class="brand__mark">MRF</span>
      <span class="brand__word">ACCOUNTANTS</span>
    </div>
    <p class="tagline">A referral from you is our greatest compliment.</p>
  </section>

  <section class="card card--front" aria-label="Card front">
    <div class="brand">
      <span class="brand__mark">MRF</span>
      <span class="brand__word">ACCOUNTANTS</span>
    </div>
    <div class="divider"></div>
    <div class="contact">
      <p class="contact__name">Marcus Elwin</p>
      <p class="contact__role">Accountant</p>
      <p class="contact__address">Level 5, 8 Corvale Ridge Road<br>Ashgrove Rise Vic 3187</p>
      <ul class="contact__lines">
        <li><svg viewBox="0 0 24 24"><path d="M6.6 10.8a15.1 15.1 0 0 0 6.6 6.6l2.2-2.2c.3-.3.7-.4 1-.2 1.1.4 2.3.6 3.6.6.6 0 1 .4 1 1V20c0 .6-.4 1-1 1A17 17 0 0 1 3 4c0-.6.4-1 1-1h3.5c.6 0 1 .4 1 1 0 1.3.2 2.5.6 3.6.1.3 0 .7-.2 1z"/></svg>9481 3057</li>
        <li><svg viewBox="0 0 24 24"><path d="M2 5h20v14H2z" fill="none" stroke="#3b7a35" stroke-width="2"/><path d="M2 5l10 8 10-8" fill="none" stroke="#3b7a35" stroke-width="2"/></svg>melwin@mrfaccountants.com.au</li>
        <li><svg viewBox="0 0 24 24"><g fill="none" stroke="#3b7a35" stroke-width="1.8"><circle cx="12" cy="12" r="9"/><ellipse cx="12" cy="12" rx="4" ry="9"/><path d="M3 12h18M5 7h14M5 17h14"/></g></svg>www.mrfaccountants.com.au</li>
      </ul>
    </div>
    <p class="tagline">The end to your tax problems begin with us.</p>
    <div class="base-band"></div>
  </section>
</body>
</html>
```